Website redesign for AI startup

Overview
We are looking to have our website https://www.hellomarno.ai/ redesigned to look much more sophisticated and modern. We would like the brand colors to be different and less or no use of the Marno bird character. We have included some example sites below for designs that we like. Please do not to use the same purple or purple at all on the site as we would like different brand colors and 'too much purple' has been the main comment.

Example sites that we like:
https://www.brightquill.com/
https://tessmark.com/
https://www.calmpathway.com/

Requirements
Redesign the following pages from our website, modeling an example site that we like:
-Home page: https://hellomarno.ai
-See an example: https://www.hellomarno.ai/example-page
-Pricing: https://www.hellomarno.ai/pricing
-Product: https://www.hellomarno.ai/how-it-works
-Portal home: https://www.hellomarno.ai/overview (you will need to create an account to view this; the account is free)
New design should be sleek, professional, and modern
The pages should contain the same content that it currently does.
Images on the pages should change to match the new designs and style.
Use different brand colors, these should look professional
The Marno bird character can be used, but it’s not required. If the bird is used, it should be rarely used and not front-and-center.
Provide both desktop and mobile designs

Target Market(s)

Small business owners

Industry/Entity Type

SaaS tool

Number of Pages Required

5+ page

Requirements
Must have
• modern and sleek design, different brand colors, mobile and web designs

```html
<!DOCTYPE html>
<html lang="en">
<head>
<meta charset="utf-8">
<title>heyMarno – Your 24/7 AI Sales Assistant</title>
<link href="https://fonts.googleapis.com/css2?family=Urbanist:wght@400;500;600;700;800&display=swap" rel="stylesheet">
<style>
:root{
  --bg:#061f33;
  --bg-deep:#04182a;
  --panel:#163a52;
  --teal:#22c3d6;
  --teal-2:#13a8c4;
  --white:#ffffff;
  --ink:#1d2b36;
  --grey:#6b7781;
  --line:#e5e8ec;
  --blue:#2f6fe0;
  --lav:#dedcf2;
  --gold:#f6c646;
}
*{box-sizing:border-box;margin:0;padding:0}
html,body{width:1200px;height:5222px;overflow:hidden}
body{
  position:relative;
  font-family:"Urbanist",sans-serif;
  color:var(--white);
  background:
    radial-gradient(ellipse 520px 700px at 1200px 1500px,rgba(34,195,214,.22),transparent 70%),
    radial-gradient(ellipse 520px 600px at 0px 2500px,rgba(34,195,214,.12),transparent 70%),
    radial-gradient(ellipse 500px 600px at 1200px 3300px,rgba(34,195,214,.16),transparent 70%),
    radial-gradient(ellipse 600px 400px at 0px 300px,rgba(34,195,214,.10),transparent 70%),
    linear-gradient(180deg,#051a2c 0%,#072640 40%,#062139 80%,var(--bg-deep) 100%);
}
.abs{position:absolute}
a{color:inherit;text-decoration:none}

/* brand name */
.brand{display:flex;align-items:center;gap:8px;font-weight:700;font-size:24px;letter-spacing:-.2px;color:var(--white);white-space:nowrap}
.brand i{width:10px;height:10px;border-radius:50%;background:var(--teal);display:inline-block;flex:none}

.nav-links{font-size:12px;font-weight:600}
.nav-links a{position:absolute;white-space:nowrap}
.pill{position:absolute;display:flex;align-items:center;justify-content:center;gap:8px;border-radius:40px;font-size:10px;font-weight:800;letter-spacing:.3px;text-transform:uppercase;white-space:nowrap}
.pill.outline{border:1.6px solid rgba(255,255,255,.85);color:var(--white)}
.pill.fill{background:var(--teal-2);color:var(--white)}
.pill.teal-outline{border:1.6px solid var(--teal);color:var(--white)}
.pill.light{background:var(--white);color:var(--ink)}
.pill svg{width:12px;height:12px}

.hero-title{font-size:50px;font-weight:700;line-height:47px;letter-spacing:-.5px;color:var(--teal)}
.hero-lead{font-size:16px;font-weight:600}
.bullets{list-style:none;font-size:12.5px;font-weight:500}
.bullets li{position:absolute;display:flex;align-items:center;gap:8px;white-space:nowrap}
.bullets svg{width:11px;height:11px}

.app{background:var(--white);border-radius:10px;overflow:hidden;color:var(--ink)}
.app-frame{border:6px solid rgba(255,255,255,.12);border-right:none;border-radius:14px 0 0 14px;overflow:hidden}
.side{background:var(--lav)}
.side-item{position:absolute;left:10px;font-size:8px;color:#4a5160;display:flex;gap:5px;align-items:center;white-space:nowrap}
.side-item i{width:7px;height:7px;border-radius:2px;background:#6c7590;display:inline-block}
.tbl{font-size:7.5px;color:#2b333b}
.tbl span{position:absolute;white-space:nowrap}

.h2{font-size:37px;font-weight:700;line-height:43px;letter-spacing:-.3px}
.body{font-size:13px;line-height:22px;color:#d7e1e8;font-weight:500}
.panel{background:var(--panel);border-radius:6px;overflow:hidden}
.help-title{font-size:30px;font-weight:500;text-align:center;width:1200px}
.feature{position:absolute;width:200px;text-align:center;font-size:14px;font-weight:600}
.feature svg{width:30px;height:30px;display:block;margin:0 auto 14px}

.node{position:absolute;width:60px;height:60px;border-radius:50%;background:var(--white);box-shadow:0 0 0 5px rgba(34,195,214,.55),0 0 18px rgba(34,195,214,.7);display:flex;align-items:center;justify-content:center;transform:translate(-50%,-50%)}
.node svg{width:26px;height:26px}
.node-label{position:absolute;font-size:12px;font-weight:600;text-align:center;width:120px;transform:translateX(-50%);line-height:14px}

.lead-card{background:var(--white);color:var(--ink);overflow:hidden}
.row{position:absolute;left:0;right:0;height:44px;display:flex;align-items:center;font-size:14px;border-bottom:1px solid var(--line)}
.cb{position:absolute;width:17px;height:17px;border:2px solid #4b545c;border-radius:2px}

.cal{background:var(--white);color:var(--ink)}
.cal .d{position:absolute;width:28px;height:28px;margin:-14px 0 0 -14px;display:flex;align-items:center;justify-content:center;font-size:11px;color:#4a525a;border-radius:50%}
.cal .d.on{background:#e8f0fd;color:var(--blue);font-weight:800}
.cal .w{position:absolute;font-size:9px;color:#4a525a;transform:translateX(-50%)}

.chip{position:absolute;height:49px;background:var(--white);color:var(--ink);border-radius:6px;display:flex;align-items:center;gap:10px;padding:0 14px;font-size:14px;font-weight:500;white-space:nowrap;overflow:hidden}
.chip i{width:22px;height:22px;border-radius:4px;display:inline-block;flex:none}
.chip.faint{background:rgba(255,255,255,.08);color:rgba(255,255,255,.2)}

.quote-card{background:var(--panel);border-radius:8px;border:1px solid rgba(255,255,255,.08);overflow:hidden}
.quote-mark{font-size:86px;font-weight:800;color:var(--teal);line-height:1}
.stars{color:var(--gold);font-size:15px;letter-spacing:2px}
.quote-text{font-size:14px;line-height:24.5px;color:#dfe7ec;font-weight:500}

.cta-band{background:linear-gradient(180deg,#12a7c4,#0e95b3)}
.cta-title{font-size:54px;font-weight:700;text-align:center;width:1200px;letter-spacing:-.5px}

.foot-links a{position:absolute;font-size:11px;font-weight:600}
.social{position:absolute;width:26px;height:26px;border-radius:50%;background:var(--white);opacity:.9}
</style>
</head>
<body>

<!-- NAV -->
<div class="abs brand" style="left:53px;top:27px"><i></i>heyMarno</div>
<nav class="nav-links">
  <a href="https://hellomarno.ai" style="left:578px;top:36px">Home</a>
  <a href="https://www.hellomarno.ai/how-it-works" style="left:628px;top:36px">Products</a>
  <a style="left:697px;top:36px">Support</a>
  <a href="https://www.hellomarno.ai/pricing" style="left:760px;top:36px">Pricing</a>
  <a style="left:817px;top:36px">FAQ</a>
  <a style="left:861px;top:36px">Referral Program</a>
</nav>
<a class="pill outline" style="left:975px;top:31px;width:66px;height:26px;font-size:9px">Login</a>
<a class="pill fill" style="left:1054px;top:31px;width:92px;height:26px;font-size:9px">Get a Demo</a>

<!-- HERO -->
<h1 class="abs hero-title" style="left:164px;top:170px;width:420px">Your 24/7 AI<br>Sales Assistant</h1>
<p class="abs hero-lead" style="left:164px;top:280px">Marno will...</p>
<ul class="bullets">
  <li style="left:164px;top:315px"><svg viewBox="0 0 12 12"><path d="M1 6.5 4.5 10 11 2" fill="none" stroke="#fff" stroke-width="1.6"/></svg>scan your website and create a fully functioning Marno in minutes</li>
  <li style="left:164px;top:340px"><svg viewBox="0 0 12 12"><path d="M1 6.5 4.5 10 11 2" fill="none" stroke="#fff" stroke-width="1.6"/></svg>engage with your leads instantly via phone, email, chat, or text</li>
  <li style="left:164px;top:366px"><svg viewBox="0 0 12 12"><path d="M1 6.5 4.5 10 11 2" fill="none" stroke="#fff" stroke-width="1.6"/></svg>qualify leads based on your criteria</li>
</ul>
<a href="https://www.hellomarno.ai/example-page" class="pill outline" style="left:164px;top:411px;width:153px;height:40px">See Examples <svg viewBox="0 0 12 12"><path d="M1 6h9M6.5 2.5 10 6l-3.5 3.5" fill="none" stroke="#fff" stroke-width="1.5"/></svg></a>
<a class="pill teal-outline" style="left:323px;top:411px;width:176px;height:40px">Create Your Marno <svg viewBox="0 0 12 12"><path d="M1 6h9M6.5 2.5 10 6l-3.5 3.5" fill="none" stroke="#fff" stroke-width="1.5"/></svg></a>

<div class="abs app-frame" style="left:602px;top:99px;width:598px;height:430px">
  <div class="app" style="position:relative;width:598px;height:418px;border-radius:8px 0 0 8px">
    <div class="abs" style="left:0;top:0;width:598px;height:50px;border-bottom:1px solid var(--line)"></div>
    <div class="abs" style="left:44px;top:20px;font-size:13px;font-weight:700;color:var(--ink)">heyMarno</div>
    <div class="abs" style="left:44px;top:35px;font-size:6px;color:var(--grey)">Beta</div>
    <div class="abs side" style="left:6px;top:53px;width:122px;height:365px">
      <div class="abs" role="img" aria-label="User profile avatar" style="left:33px;top:22px;width:56px;height:56px;border-radius:50%;background:linear-gradient(135deg,#f2c9b5,#e79980)"></div>
      <div class="abs" style="left:0;width:122px;top:92px;text-align:center;font-size:6.5px;color:#4a5160">Lee The Roofer</div>
      <div class="side-item" style="top:124px"><i></i>Overview</div>
      <div class="side-item" style="top:148px"><i></i>Settings</div>
      <div class="abs" style="left:0;top:166px;width:122px;height:22px;background:#fff"></div>
      <div class="side-item" style="top:173px;font-weight:700;color:var(--ink)"><i></i>Contacts</div>
      <div class="side-item" style="top:199px"><i></i>Reports</div>
      <div class="side-item" style="top:223px"><i></i>Billing</div>
      <div class="side-item" style="top:249px"><i></i>Referrals</div>
    </div>
    <div class="abs" style="left:142px;top:92px;font-size:18px;font-weight:500">Contacts</div>
    <div class="abs" style="left:142px;top:122px;width:460px;height:1px;background:var(--line)"></div>
    <div class="abs" style="left:142px;top:165px;width:460px;height:118px;border:1px solid var(--line);border-right:none"></div>
    <div class="tbl">
      <span style="left:160px;top:176px;width:8px;height:8px;border:1px solid #555"></span>
      <span style="left:180px;top:176px">Name</span><span style="left:225px;top:176px">Email</span><span style="left:426px;top:176px">Status</span><span style="left:470px;top:176px">Last Activity</span>
      <span style="left:160px;top:199px;width:8px;height:8px;border:1px solid #555"></span>
      <span style="left:180px;top:199px">Petra</span><span style="left:225px;top:199px">petra@mailbox.test</span><span style="left:426px;top:199px">New</span><span style="left:470px;top:199px">03/22/2024 03:16 PM</span>
      <span style="left:160px;top:221px;width:8px;height:8px;border:1px solid #555"></span>
      <span style="left:180px;top:221px">Ansel</span><span style="left:225px;top:221px">ansel@inbox.test</span><span style="left:426px;top:221px">New</span><span style="left:470px;top:221px">03/22/2024 03:16 PM</span>
      <span style="left:160px;top:246px;width:8px;height:8px;border:1px solid #555"></span>
      <span style="left:180px;top:246px">Greta</span><span style="left:350px;top:246px">555-010-2847</span><span style="left:426px;top:246px">New</span><span style="left:470px;top:246px">03/22/2024 03:11 PM</span>
      <span style="left:480px;top:268px;color:var(--grey)">Rows per page: 25 ▾</span>
    </div>
    <div class="abs" style="left:314px;top:183px;width:73px;height:52px;background:#2a2d31;border-radius:4px;display:flex;flex-direction:column;align-items:center;justify-content:center;gap:6px">
      <div style="width:16px;height:16px;border-radius:50%;background:#e2302b"></div>
      <div style="font-size:7px;font-weight:700;color:#fff">PLAY VIDEO</div>
    </div>
  </div>
</div>

<!-- HERE TO HELP -->
<h2 class="abs help-title" style="left:0;top:586px">HeyMarno Is Here To Help</h2>
<div class="feature" style="left:202px;top:708px">
  <svg viewBox="0 0 30 30" fill="none" stroke="#22c3d6" stroke-width="1.6"><path d="M15 5a7 7 0 0 0-4 12.7V21h8v-3.3A7 7 0 0 0 15 5z"/><path d="M12 24h6M15 1v2M5 11H3M27 11h-2M7 4l1.5 1.5M23 4l-1.5 1.5"/></svg>
  Company Knowledge</div>
<div class="feature" style="left:405px;top:708px">
  <svg viewBox="0 0 30 30" fill="none" stroke="#22c3d6" stroke-width="1.6"><path d="M27 3 3 13l9 4 4 9z"/><path d="M27 3 12 17"/></svg>
  Team Acceleration</div>
<div class="feature" style="left:603px;top:708px">
  <svg viewBox="0 0 30 30" fill="none" stroke="#22c3d6" stroke-width="1.6"><rect x="8" y="8" width="14" height="14" rx="2"/><rect x="12" y="12" width="6" height="6"/><path d="M12 4v4M18 4v4M12 22v4M18 22v4M4 12h4M4 18h4M22 12h4M22 18h4"/></svg>
  AI-Assisted Content</div>
<div class="feature" style="left:802px;top:708px">
  <svg viewBox="0 0 30 30" fill="none" stroke="#22c3d6" stroke-width="1.6"><circle cx="13" cy="13" r="9"/><path d="m20 20 7 7M9 14l3 3 5-6"/></svg>
  Analytics &amp; Insights</div>

<!-- 24/7 ENGAGEMENT -->
<h2 class="abs h2" style="left:164px;top:1038px">24/7 Customer<br>Engagement</h2>
<p class="abs body" style="left:164px;top:1150px;width:290px">Marno interacts with your leads across email, chatbot, phone, and text around the clock.</p>
<a href="https://www.hellomarno.ai/example-page" class="abs" style="left:164px;top:1208px;font-size:13px;font-weight:700;color:var(--teal);text-decoration:underline">See an example here.</a>

<div class="abs panel" style="left:537px;top:932px;width:499px;height:402px">
  <svg class="abs" style="left:0;top:0" width="499" height="402"><circle cx="247" cy="215" r="137" fill="none" stroke="rgba(34,195,214,.25)" stroke-width="1.5"/></svg>
  <div class="abs" role="img" aria-label="Assistant mascot in a glowing circle" style="left:197px;top:165px;width:100px;height:100px;border-radius:50%;background:radial-gradient(circle,#2fa9c4 0%,#0f3a52 70%);box-shadow:0 0 0 5px rgba(34,195,214,.35),0 0 30px rgba(34,195,214,.5)"></div>
  <div class="node" style="left:249px;top:77px"><svg viewBox="0 0 26 26" fill="none" stroke="#163a52" stroke-width="1.8"><rect x="5" y="3" width="16" height="20" rx="2"/><path d="M9 9h8M9 13h8M9 17h5"/></svg></div>
  <div class="node-label" style="left:249px;top:121px">Texting</div>
  <div class="node" style="left:144px;top:134px"><svg viewBox="0 0 26 26" fill="none" stroke="#163a52" stroke-width="1.8"><path d="M6 3h4l2 5-3 2a12 12 0 0 0 7 7l2-3 5 2v4a2 2 0 0 1-2 2A18 18 0 0 1 4 5a2 2 0 0 1 2-2z"/></svg></div>
  <div class="node-label" style="left:144px;top:178px">Phone Calls</div>
  <div class="node" style="left:351px;top:134px"><svg viewBox="0 0 26 26" fill="none" stroke="#163a52" stroke-width="1.8"><rect x="3" y="6" width="20" height="14" rx="1"/><path d="m3 6 10 8 10-8"/></svg></div>
  <div class="node-label" style="left:351px;top:178px">Email</div>
  <div class="node" style="left:112px;top:250px"><svg viewBox="0 0 26 26" fill="none" stroke="#163a52" stroke-width="1.8"><path d="M4 4h18v14H10l-5 4v-4H4z"/><path d="M8 9h10M8 13h7"/></svg></div>
  <div class="node-label" style="left:112px;top:294px">Try out Chat</div>
  <div class="node" style="left:387px;top:250px"><svg viewBox="0 0 26 26" fill="none" stroke="#163a52" stroke-width="1.8"><circle cx="13" cy="9" r="5"/><path d="M4 23a9 9 0 0 1 18 0z"/></svg></div>
  <div class="node-label" style="left:387px;top:294px">Lead<br>Management</div>
</div>

<!-- LEAD QUALIFICATION -->
<div class="abs panel" style="left:162px;top:1411px;width:499px;height:403px">
  <div class="abs lead-card" style="left:28px;top:22px;width:443px;height:381px;border-radius:4px 4px 0 0">
    <svg class="abs" style="left:142px;top:44px" width="160" height="18" fill="none" stroke="#555" stroke-width="1.6">
      <circle cx="8" cy="8" r="5"/><path d="m12 12 4 4"/>
      <path d="M44 14h12a4 4 0 0 0 0-8 6 6 0 0 0-11-1 4 4 0 0 0-1 9z" fill="#555"/>
      <path d="M80 3v12M85 3v12M90 3v12M95 3v12" stroke-width="2.4"/>
      <path d="M118 4h14M121 9h8M124 14h2"/>
    </svg>
    <div class="abs" style="left:20px;right:20px;top:0;height:381px">
      <div class="row" style="top:96px;font-weight:600"><span class="cb" style="left:13px"></span><span style="position:absolute;left:76px">Name</span><span style="position:absolute;left:224px">Qualification ↓</span></div>
      <div class="row" style="top:140px;color:#2b333b"><span class="cb" style="left:13px"></span><span style="position:absolute;left:76px">Owen Hartley</span><span style="position:absolute;left:224px">qualified</span></div>
      <div class="row" style="top:229px"><span class="cb" style="left:13px"></span><span style="position:absolute;left:76px">Miles Ashford</span><span style="position:absolute;left:224px">qualified</span></div>
      <div class="row" style="top:273px"><span class="cb" style="left:13px"></span><span style="position:absolute;left:76px">Rafael Cortes</span><span style="position:absolute;left:224px">qualified</span></div>
      <div class="row" style="top:318px"><span class="cb" style="left:13px"></span><span style="position:absolute;left:76px">Nora Bellamy</span><span style="position:absolute;left:224px">disqualified</span></div>
    </div>
  </div>
  <div class="abs" style="left:114px;top:190px;width:385px;height:50px;background:#fff;border-radius:3px;box-shadow:0 6px 20px rgba(0,0,0,.25);color:var(--ink);font-size:14px">
    <svg class="abs" style="left:22px;top:15px" width="20" height="20" fill="none" stroke="#22a7c4" stroke-width="2"><rect x="1" y="1" width="18" height="18" rx="2"/><path d="m5 10 4 4 7-8"/></svg>
    <span class="abs" style="left:60px;top:15px">Ivo Brandt</span>
    <span class="abs" style="left:168px;top:17px">qualified</span>
    <span class="abs pill fill" style="left:264px;top:14px;width:86px;height:22px;font-size:7px">Add Contact →</span>
  </div>
</div>
<h2 class="abs h2" style="left:728px;top:1490px">Lead Qualification<br>&amp; Prioritization</h2>
<p class="abs body" style="left:728px;top:1594px;width:260px">Marno captures, engages, and qualifies leads, helping you focus on the most promising opportunities.</p>
<a class="pill teal-outline" style="left:728px;top:1688px;width:177px;height:40px">Create Your Marno <svg viewBox="0 0 12 12"><path d="M1 6h9M6.5 2.5 10 6l-3.5 3.5" fill="none" stroke="#fff" stroke-width="1.5"/></svg></a>

<!-- SCHEDULING -->
<h2 class="abs h2" style="left:164px;top:1968px">Automated<br>Scheduling</h2>
<p class="abs body" style="left:164px;top:2072px;width:275px">Marno books meetings with qualified leads directly on your calendar, streamlining your sales process.</p>
<a class="pill teal-outline" style="left:164px;top:2165px;width:176px;height:39px">Create Your Marno <svg viewBox="0 0 12 12"><path d="M1 6h9M6.5 2.5 10 6l-3.5 3.5" fill="none" stroke="#fff" stroke-width="1.5"/></svg></a>

<div class="abs panel" style="left:582px;top:1889px;width:385px;height:402px"></div>
<div class="abs cal" style="left:614px;top:1913px;width:323px;height:355px;overflow:hidden;border-radius:2px">
  <div class="abs" style="left:31px;top:23px;font-size:14px;font-weight:700">Select a Date &amp; Time</div>
  <div class="abs" style="left:87px;top:72px;font-size:12px;color:#777">‹</div>
  <div class="abs" style="left:128px;top:72px;font-size:11px">July 2023</div>
  <div class="abs" style="left:223px;top:68px;width:22px;height:22px;border-radius:50%;background:#e8f0fd;color:var(--blue);font-size:12px;text-align:center;line-height:21px">›</div>
  <div class="w" style="left:81px;top:114px">MON</div><div class="w" style="left:122px;top:114px">TUE</div><div class="w" style="left:162px;top:114px">WED</div><div class="w" style="left:203px;top:114px">THU</div><div class="w" style="left:245px;top:114px">FRI</div><div class="w" style="left:286px;top:114px">SAT</div>
  <div class="d" style="left:286px;top:146px">1</div>
  <div class="d" style="left:41px;top:187px">2</div><div class="d" style="left:81px;top:187px">3</div><div class="d" style="left:122px;top:187px">4</div><div class="d" style="left:162px;top:187px">5</div><div class="d" style="left:203px;top:187px">6</div><div class="d" style="left:245px;top:187px">7</div><div class="d" style="left:286px;top:187px">8</div>
  <div class="d" style="left:41px;top:228px">9</div><div class="d" style="left:81px;top:228px">10</div><div class="d" style="left:122px;top:228px">11</div>
  <div class="d" style="left:41px;top:270px">16</div><div class="d on" style="left:81px;top:270px">17</div><div class="d on" style="left:122px;top:270px">18</div><div class="d" style="left:162px;top:270px">19</div><div class="d" style="left:203px;top:270px">20</div><div class="d" style="left:245px;top:270px">21</div><div class="d" style="left:286px;top:270px">22</div>
  <div class="d" style="left:41px;top:311px">23</div><div class="d on" style="left:81px;top:311px">24</div><div class="d on" style="left:122px;top:311px">25</div><div class="d on" style="left:162px;top:311px">26</div><div class="d on" style="left:203px;top:311px">27</div><div class="d on" style="left:245px;top:311px">28</div><div class="d" style="left:286px;top:311px">29</div>
  <div class="d" style="left:41px;top:351px">30</div><div class="d on" style="left:81px;top:351px">31</div>
</div>
<div class="abs" style="left:576px;top:1972px;width:105px;height:94px;background:#fff;border-radius:4px;box-shadow:0 6px 18px rgba(0,0,0,.3)">
  <div class="abs" style="left:10px;top:16px;width:80px;height:3px;background:#2f4a8a"></div>
  <div class="abs" style="left:10px;top:30px;width:6px;height:6px;border-radius:50%;background:#22c3d6"></div><div class="abs" style="left:22px;top:31px;width:70px;height:3px;background:#c9d0da"></div>
  <div class="abs" style="left:10px;top:46px;width:6px;height:6px;border-radius:50%;background:#e2587a"></div><div class="abs" style="left:22px;top:47px;width:70px;height:3px;background:#2f4a8a"></div>
  <div class="abs" style="left:10px;top:62px;width:6px;height:6px;border-radius:50%;background:#22c3d6"></div><div class="abs" style="left:22px;top:63px;width:70px;height:3px;background:#c9d0da"></div>
  <div class="abs" style="left:22px;top:76px;width:50px;height:3px;background:#2f4a8a"></div>
</div>
<div class="abs" style="left:764px;top:2130px;width:272px;height:61px;background:#fff;border-radius:4px;box-shadow:0 6px 18px rgba(0,0,0,.3);color:var(--ink)">
  <div class="abs" style="left:24px;top:12px;font-size:11px;font-weight:700">Time zone</div>
  <div class="abs" style="left:24px;top:33px;font-size:9px;white-space:nowrap">◍ &nbsp;Pacific Time - US &amp; Canada (8:40am) ▾</div>
</div>

<!-- RAPID AI TRAINING -->
<div class="abs panel" style="left:162px;top:2368px;width:499px;height:403px">
  <div class="abs" role="img" aria-label="Illustration of a person smiling at a computer desk in a bright office" style="left:28px;top:24px;width:443px;height:356px;background:linear-gradient(180deg,#d9d6ef 0%,#ecebf8 55%,#ffffff 56%,#ffffff 100%)"></div>
  <div class="abs" style="left:309px;top:31px;width:120px;height:120px;border-radius:50%;background:var(--gold);display:flex;align-items:center;justify-content:center;text-align:center;transform:rotate(18deg);font-size:20px;font-weight:800;line-height:21px;color:#fff">Free 14<br>Day Trial</div>
</div>
<h2 class="abs h2" style="left:722px;top:2443px">Rapid and<br>Effective AI<br>Training</h2>
<p class="abs body" style="left:722px;top:2581px;width:275px">Marno analyzes your website, allowing Marno to provide accurate and up-to-date information to your leads.</p>
<a class="pill teal-outline" style="left:722px;top:2676px;width:177px;height:40px">Create Your Marno <svg viewBox="0 0 12 12"><path d="M1 6h9M6.5 2.5 10 6l-3.5 3.5" fill="none" stroke="#fff" stroke-width="1.5"/></svg></a>

<!-- CUSTOMIZE -->
<h2 class="abs h2" style="left:164px;top:2927px">Customize Your<br>Assistant</h2>
<p class="abs body" style="left:164px;top:3030px;width:275px">Change your phone number, email, how Marno engages with your leads, and much more, turning every interaction into an opportunity.</p>
<a class="pill teal-outline" style="left:164px;top:3146px;width:176px;height:40px">Create Your Marno <svg viewBox="0 0 12 12"><path d="M1 6h9M6.5 2.5 10 6l-3.5 3.5" fill="none" stroke="#fff" stroke-width="1.5"/></svg></a>

<div class="abs panel" style="left:537px;top:2846px;width:499px;height:405px">
  <div class="abs app" style="left:29px;top:27px;width:443px;height:358px;border-radius:4px">
    <div class="abs" style="left:0;top:0;width:443px;height:22px;border-bottom:1px solid var(--line)"></div>
    <div class="abs" style="left:8px;top:6px;font-size:9px;font-weight:700">heyMarno</div>
    <div class="abs side" style="left:0;top:22px;width:90px;height:336px">
      <div class="abs" role="img" aria-label="Assistant avatar" style="left:22px;top:12px;width:44px;height:44px;border-radius:6px;background:linear-gradient(135deg,#6cc3d6,#3a7f9a)"></div>
      <div class="abs" style="left:0;width:90px;top:62px;text-align:center;font-size:5px;color:#555">Your Marno</div>
      <div class="side-item" style="top:80px;font-size:5.5px">Overview</div>
      <div class="side-item" style="top:94px;font-size:5.5px">Settings</div>
      <div class="side-item" style="top:108px;font-size:5px;left:18px">Basic Info</div>
      <div class="side-item" style="top:120px;font-size:5px;left:18px">Contact Options</div>
      <div class="side-item" style="top:132px;font-size:5px;left:18px">Chatbot</div>
      <div class="side-item" style="top:144px;font-size:5px;left:18px">Email</div>
      <div class="side-item" style="top:304px;font-size:5.5px">Contacts</div>
      <div class="side-item" style="top:318px;font-size:5.5px">Reports</div>
    </div>
    <div class="abs" style="left:104px;top:38px;font-size:13px">Settings</div>
    <div class="abs" style="left:104px;top:56px;font-size:6px;color:#555">Phone/Text</div>
    <svg class="abs" style="left:110px;top:84px" width="320" height="14">
      <line x1="6" y1="7" x2="314" y2="7" stroke="#c8cde8" stroke-width="1"/>
      <g fill="#fff" stroke="#5a6fd0" stroke-width="1.4"><circle cx="6" cy="7" r="4"/><circle cx="50" cy="7" r="4"/><circle cx="94" cy="7" r="4"/><circle cx="138" cy="7" r="4"/><circle cx="182" cy="7" r="4"/><circle cx="226" cy="7" r="4"/><circle cx="270" cy="7" r="4"/><circle cx="314" cy="7" r="4"/></g>
    </svg>
    <div class="abs" style="left:130px;top:138px;font-size:5.5px;color:#5a6fd0;font-weight:700">Your Marno phone number: (555) 010-3391</div>
    <div class="abs" style="left:130px;top:164px;font-size:5.5px;font-weight:700">Choose a local area code</div>
    <div class="abs" style="left:130px;top:172px;width:300px;font-size:5px;color:#666;line-height:7px">Pick a local code and we will set up a fresh number for your assistant right away today.</div>
    <div class="abs" style="left:130px;top:190px;width:52px;height:10px;border-radius:2px;background:#5a6fd0;font-size:4.5px;color:#fff;text-align:center;line-height:10px">Confirm area code</div>
    <div class="abs" style="left:130px;top:222px;font-size:5.5px;font-weight:700">Choose your Marno's voice and phone greeting</div>
    <div class="abs" role="img" aria-label="Voice option portrait" style="left:248px;top:244px;width:26px;height:26px;border-radius:50%;background:#d9b9a5"></div><div class="abs" style="left:280px;top:250px;font-size:4.5px;color:#555">Ada - calm and clear</div>
    <div class="abs" role="img" aria-label="Voice option portrait" style="left:330px;top:244px;width:26px;height:26px;border-radius:50%;background:#c9a58f"></div><div class="abs" style="left:362px;top:250px;font-size:4.5px;color:#555">Jules - bright tone</div>
    <div class="abs" role="img" aria-label="Voice option portrait" style="left:130px;top:284px;width:26px;height:26px;border-radius:50%;background:#b58c74"></div><div class="abs" style="left:162px;top:292px;font-size:4.5px;color:#555">Kai - warm and even</div>
    <div class="abs" role="img" aria-label="Voice option portrait" style="left:248px;top:284px;width:26px;height:26px;border-radius:50%;background:#e0c2ae"></div><div class="abs" style="left:280px;top:290px;font-size:4.5px;color:#555">Rio - relaxed pace</div>
    <div class="abs" role="img" aria-label="Voice option portrait" style="left:330px;top:284px;width:26px;height:26px;border-radius:50%;background:#a97f68"></div><div class="abs" style="left:362px;top:290px;font-size:4.5px;color:#555">Skye - upbeat style</div>
    <div class="abs" style="left:130px;top:336px;font-size:4.5px;color:#555">Hi, I'm the AI assistant for your team.</div>
    <div class="abs" style="left:264px;top:333px;width:46px;height:11px;border-radius:2px;background:#5a6fd0;font-size:4.5px;color:#fff;text-align:center;line-height:11px">Save and Play</div>
  </div>
  <div class="abs" style="left:10px;top:255px;width:136px;height:57px;background:#fff;border-radius:4px;box-shadow:0 6px 18px rgba(0,0,0,.3);color:var(--ink)">
    <div class="abs" role="img" aria-label="Voice option portrait" style="left:10px;top:12px;width:32px;height:32px;border-radius:50%;background:#d4a88f"></div>
    <div class="abs" style="left:50px;top:16px;font-size:7.5px;line-height:10px;width:80px">Lena - upbeat and lively</div>
  </div>
</div>

<!-- INTEGRATIONS -->
<div class="abs panel" style="left:162px;top:3331px;width:499px;height:399px">
  <div class="chip faint" style="left:-20px;top:26px;width:140px"><i style="background:rgba(255,255,255,.1)"></i>Mailcraft</div>
  <div class="chip faint" style="left:130px;top:26px;width:250px"><i style="background:rgba(255,255,255,.1)"></i>Orbit CRM Suite</div>
  <div class="chip faint" style="left:390px;top:26px;width:140px"></div>
  <div class="chip" style="left:35px;top:102px;width:202px"><i style="background:#2d7fc9"></i>Mailcraft</div>
  <div class="chip" style="left:258px;top:102px;width:146px"><i style="background:#2a2f33"></i>Sendwell</div>
  <div class="chip" style="left:424px;top:102px;width:140px"><i style="background:#ef7a42"></i>Hubline</div>
  <div class="chip" style="left:-10px;top:179px;width:148px"><i style="background:#1f2429"></i>Dealflow</div>
  <div class="chip" style="left:166px;top:179px;width:142px"><i style="background:#6cc04a"></i>Datarail</div>
  <div class="chip" style="left:337px;top:179px;width:152px"><i style="background:#1b96d8"></i>Cloudsale</div>
  <div class="chip" style="left:63px;top:254px;width:134px"><i style="background:#7bb342"></i>Storely</div>
  <div class="chip" style="left:221px;top:254px;width:126px"><i style="background:#f0692a"></i>Linkzy</div>
  <div class="chip" style="left:369px;top:254px;width:150px"><i style="background:#5b4bc4"></i>Markpoint</div>
  <div class="chip faint" style="left:0;top:326px;width:160px"><i style="background:rgba(255,255,255,.1)"></i>Dealflow</div>
  <div class="chip faint" style="left:176px;top:326px;width:150px"><i style="background:rgba(255,255,255,.1)"></i>Linkzy</div>
</div>
<div class="abs" style="left:142px;top:3302px;width:106px;height:106px;border-radius:50%;background:var(--teal-2);border:4px dashed rgba(255,255,255,.45);display:flex;align-items:center;justify-content:center;text-align:center;font-size:21px;font-weight:800;line-height:22px">+1000s<br>More</div>
<h2 class="abs h2" style="left:728px;top:3403px">Seamless Tool<br>Integration</h2>
<p class="abs body" style="left:728px;top:3507px;width:275px">heyMarno's streamlined tool integrations effortlessly sync with your existing business tools and platforms, ensuring a smooth and seamless setup.</p>
<a class="pill teal-outline" style="left:728px;top:3629px;width:177px;height:40px">Create Your Marno <svg viewBox="0 0 12 12"><path d="M1 6h9M6.5 2.5 10 6l-3.5 3.5" fill="none" stroke="#fff" stroke-width="1.5"/></svg></a>

<!-- WAVE BAND -->
<div class="abs" role="img" aria-label="Flowing teal wave of light lines" style="left:0;top:3790px;width:1200px;height:205px;background:radial-gradient(ellipse 600px 80px at 600px 100px,rgba(34,195,214,.45),rgba(34,195,214,.12) 60%,transparent 80%)"></div>

<!-- TESTIMONIALS -->
<h2 class="abs" style="left:0;top:4040px;width:1200px;text-align:center;font-size:46px;font-weight:700;line-height:52px;letter-spacing:-.4px">Hundreds of People<br>Already Love Us</h2>
<div class="abs quote-card" style="left:245px;top:4192px;width:578px;height:223px">
  <div class="abs quote-mark" style="left:45px;top:30px">“</div>
  <div class="abs stars" style="left:132px;top:34px">★★★★★</div>
  <p class="abs quote-text" style="left:132px;top:64px;width:420px">I've tried several different AI Sales Assistants, and heyMarno is truly the best one out there offering AI responses across text, email, phone calls and a chatbot for only $50 a month.</p>
  <p class="abs quote-text" style="left:132px;top:153px">~ <b>Dario Velez</b>, Product Manager</p>
</div>
<div class="abs quote-card" style="left:876px;top:4192px;width:324px;height:223px;opacity:.45;border-radius:8px 0 0 8px">
  <div class="abs quote-mark" style="left:45px;top:30px">“</div>
  <div class="abs stars" style="left:132px;top:34px">★★★★★</div>
  <p class="abs quote-text" style="left:132px;top:64px;width:420px">I've tried several different AI Sales Assistants, and heyMarno is truly the best one out there offering AI responses across text, email, phone calls and a chatbot for only $50 a month.</p>
  <p class="abs quote-text" style="left:132px;top:153px;white-space:nowrap">~ <b>Dario Velez</b>, Product Manager</p>
</div>
<div class="abs" style="left:564px;top:4447px;width:8px;height:4px;border-radius:2px;background:rgba(255,255,255,.3)"></div>
<div class="abs" style="left:584px;top:4447px;width:8px;height:4px;border-radius:2px;background:#fff"></div>
<div class="abs" style="left:604px;top:4447px;width:8px;height:4px;border-radius:2px;background:#fff"></div>
<div class="abs" style="left:625px;top:4447px;width:8px;height:4px;border-radius:2px;background:#fff"></div>

<!-- CTA -->
<section class="abs cta-band" style="left:0;top:4520px;width:1200px;height:288px">
  <h2 class="abs cta-title" style="left:0;top:70px">Set Up Your Own Marno</h2>
  <a href="https://www.hellomarno.ai/example-page" class="pill outline" style="left:432px;top:162px;width:154px;height:41px">See Examples <svg viewBox="0 0 12 12"><path d="M1 6h9M6.5 2.5 10 6l-3.5 3.5" fill="none" stroke="#fff" stroke-width="1.5"/></svg></a>
  <a class="pill light" style="left:592px;top:162px;width:176px;height:41px">Create Your Marno <svg viewBox="0 0 12 12"><path d="M1 6h9M6.5 2.5 10 6l-3.5 3.5" fill="none" stroke="#1d2b36" stroke-width="1.5"/></svg></a>
</section>

<!-- FOOTER -->
<div class="abs brand" style="left:162px;top:4878px;font-size:28px"><i></i>heyMarno</div>
<h3 class="abs" style="left:164px;top:4962px;font-size:27px;font-weight:700;line-height:33px">Stay up to date on our<br>news and progress</h3>
<div class="abs" style="left:164px;top:5046px;width:314px;height:36px;border-bottom:1px solid rgba(255,255,255,.25);display:flex;align-items:center;gap:8px;font-size:11px;color:#c8d4dc;padding-left:10px">
  <svg width="12" height="10" fill="none" stroke="#c8d4dc" stroke-width="1.2"><rect x=".6" y=".6" width="10.8" height="8.8"/><path d="m.6.6 5.4 4.4L11.4.6"/></svg>Enter your email
</div>
<div class="abs" style="left:444px;top:5049px;width:32px;height:30px;background:#fff;border-radius:2px;display:flex;align-items:center;justify-content:center"><svg width="12" height="12" viewBox="0 0 12 12"><path d="M1 6h9M6.5 2.5 10 6l-3.5 3.5" fill="none" stroke="#1d2b36" stroke-width="1.5"/></svg></div>
<nav class="foot-links">
  <a href="https://hellomarno.ai" style="left:936px;top:4895px">Home</a>
  <a href="https://www.hellomarno.ai/how-it-works" style="left:936px;top:4929px">Products</a>
  <a style="left:936px;top:4963px">Support</a>
  <a href="https://www.hellomarno.ai/pricing" style="left:936px;top:4997px">Pricing</a>
  <a style="left:936px;top:5032px">FAQ</a>
  <a style="left:936px;top:5066px">Referral Program</a>
</nav>
<p class="abs" style="left:164px;top:5158px;font-size:9px;color:#c8d4dc">© 2024 HeyMarno.ai. All rights reserved.</p>
<div class="social" style="left:895px;top:5152px"></div>
<div class="social" style="left:932px;top:5152px"></div>
<div class="social" style="left:970px;top:5152px"></div>
<div class="social" style="left:1009px;top:5152px"></div>

</body>
</html>
```